Eye-Catching, Direct Marketing Residential Painting Flyer!

I am run a residential painting business and am looking for a flyer to be designed to mailout to potential customers.
I want the copy/wording to be designed similar to this flyer.

It's important that the person reading the flyer gets the benefits we're promoting which is why I want the wording/copy to be almost identical to the flyer attached.

However, the structure will be different. The flyer will be a postcard thick, 5 x11.5.
Double sided.

The name of the company is Brightwall Coaters.

I would also like the prominent colour to either be light green or orange.

Target Market(s)

Home Owners between the age of 45-80.

Industry/Entity Type

Painting And Decorating

Font styles to use
Serif

Colors
f68d4d
faa54b
f78f20
f37122
9bcb3c
abd037
cadf82

Requirements
Must have
• Excellent Eye-Catching Design
• Benefits Visibly Promoted
• Action Taking Incentive- Call Now for FREE Window Cleaning and FREE Painting Estimate
Should not have
• Crowded wording

```html
<!DOCTYPE html>
<html lang="en">
<head>
<meta charset="utf-8">
<title>Brightwall Coaters – Rack Card Front and Back</title>
<link href="https://fonts.googleapis.com/css2?family=Oswald:wght@500;600;700&family=Lato:ital,wght@0,400;0,700;1,700;1,900&family=Kaushan+Script&display=swap" rel="stylesheet">
<style>
  :root{
    --orange-deep:#f37122;
    --orange:#f78f20;
    --orange-light:#faa54b;
    --orange-soft:#f68d4d;
    --rust:#a8420f;
    --rust-dark:#7a2c08;
    --green:#9bcb3c;
    --green-mid:#abd037;
    --green-pale:#cadf82;
    --ink:#1f1f1f;
    --night:#1d2433;
    --paper:#ececec;
    --white:#ffffff;
    --stage:#b9b9b9;
  }
  *{box-sizing:border-box;margin:0;padding:0}
  html,body{width:1200px;height:1200px;overflow:hidden}
  body{background:var(--stage);position:relative;font-family:"Lato",sans-serif}
  .card{position:absolute;top:104px;width:450px;height:1036px;overflow:hidden;background:var(--paper);box-shadow:0 6px 18px rgba(0,0,0,.25)}
  .card--front{left:143px}
  .card--back{left:623px}
  .card__art{position:absolute;inset:0;width:100%;height:100%}
  .abs{position:absolute;left:0;right:0;text-align:center;white-space:nowrap}

  .brand-name{font-family:"Oswald",sans-serif;font-weight:700;color:var(--white);line-height:1;white-space:nowrap}
  .card--front .brand-name{top:334px;font-size:48px}
  .tagline{top:420px;font-family:"Oswald",sans-serif;font-weight:600;font-size:25px;color:var(--green);letter-spacing:-.2px;transform:scaleX(.92);text-shadow:1px 1px 0 var(--white)}

  .headline{font-family:"Oswald",sans-serif;font-weight:600;color:var(--white);line-height:1;
    text-shadow:2px 0 0 var(--rust-dark),-2px 0 0 var(--rust-dark),0 2px 0 var(--rust-dark),0 -2px 0 var(--rust-dark),2px 2px 0 var(--rust-dark),-2px -2px 0 var(--rust-dark),2px -2px 0 var(--rust-dark),-2px 2px 0 var(--rust-dark)}
  .headline--lead{top:538px;font-size:40px;font-weight:500;transform:scaleX(.9)}
  .headline--main{top:588px;font-size:40px;font-weight:700;transform:scaleX(.86)}
  .headline--again{top:636px;font-family:"Kaushan Script",cursive;font-weight:400;font-size:40px}

  .problem{top:718px;font-family:"Kaushan Script",cursive;font-size:24px;color:var(--white);line-height:1}
  .problem-copy{top:758px;font-size:16.5px;line-height:22px;color:var(--ink);white-space:normal}

  .estimates{top:816px;display:flex;align-items:center;gap:8px;font-family:"Lato",sans-serif;font-weight:900;font-size:27px;letter-spacing:1px;color:var(--ink);line-height:1}
  .estimates::before,.estimates::after{content:"";flex:1;height:1.5px;background:var(--ink)}
  .phone{top:842px;font-family:"Oswald",sans-serif;font-weight:700;font-size:76px;line-height:1;color:var(--white);
    text-shadow:3px 0 0 var(--rust-dark),-3px 0 0 var(--rust-dark),0 3px 0 var(--rust-dark),0 -3px 0 var(--rust-dark),2px 2px 0 var(--rust-dark),-2px -2px 0 var(--rust-dark),2px -2px 0 var(--rust-dark),-2px 2px 0 var(--rust-dark)}

  .links{top:970px;left:100px;right:auto;text-align:left;font-size:16.5px;line-height:21px;color:var(--white)}
  .links__row{display:flex;align-items:center;gap:6px}
  .links__dot{width:13px;height:13px;border-radius:50%;background:var(--green);flex:none}

  .card--back .brand{top:22px;left:66px;right:auto;display:flex;align-items:center;gap:12px}
  .brand__disc{width:68px;height:68px;border-radius:50%;background:var(--white);border:4px solid var(--orange-deep);flex:none}
  .card--back .brand-name{font-size:31px;color:var(--orange-deep)}

  .offer-title{top:380px;font-family:"Oswald",sans-serif;font-weight:700;font-size:44px;line-height:1;color:var(--white);transform:scaleX(.9);
    text-shadow:2px 0 0 var(--rust-dark),-2px 0 0 var(--rust-dark),0 2px 0 var(--rust-dark),0 -2px 0 var(--rust-dark),2px 2px 0 var(--rust-dark),-2px -2px 0 var(--rust-dark)}
  .offer{left:73px;right:69px;color:var(--white);line-height:1.35;white-space:normal}
  .offer--windows{top:468px;font-size:15px;line-height:23px}
  .offer--design{top:646px;font-size:14px;line-height:21px}
  .offer strong{display:block;font-style:italic;font-weight:900;font-size:20px;line-height:28px}
  .offer--design strong{font-size:19px;line-height:25px}
</style>
</head>
<body>

<section class="card card--front" aria-label="Front of rack card">
  <svg class="card__art" viewBox="0 0 450 1036">
    <defs>
      <linearGradient id="fNight" x1="0" y1="0" x2="1" y2="1">
        <stop offset="0" stop-color="#2c3446"/><stop offset="1" stop-color="#141a26"/>
      </linearGradient>
      <linearGradient id="fPhoto" x1="0" y1="0" x2="1" y2="1">
        <stop offset="0" stop-color="#9b5a3c"/><stop offset=".55" stop-color="#b9b4ae"/><stop offset="1" stop-color="#8f8a86"/>
      </linearGradient>
      <radialGradient id="fOrange" cx=".5" cy=".35" r=".75">
        <stop offset="0" stop-color="#faa54b"/><stop offset=".6" stop-color="#f78f20"/><stop offset="1" stop-color="#e4601a"/>
      </radialGradient>
      <linearGradient id="fFoot" x1="0" y1="0" x2="0" y2="1">
        <stop offset="0" stop-color="#3a3a3a"/><stop offset="1" stop-color="#161616"/>
      </linearGradient>
      <linearGradient id="fRust" x1="0" y1="0" x2="1" y2="0">
        <stop offset="0" stop-color="#b24a12"/><stop offset="1" stop-color="#8c3408"/>
      </linearGradient>
    </defs>
    <path d="M0 300 Q60 240 450 250 V600 H0Z" fill="url(#fNight)" role="img" aria-label="Dark paint roller texture"/>
    <path d="M0 0 H450 V232 Q300 292 190 270 Q80 250 0 178Z" fill="url(#fPhoto)" role="img" aria-label="Photo of three painters standing on a freshly stained deck"/>
    <path d="M0 178 Q80 250 190 270 Q300 292 450 232 V252 Q300 312 170 292 Q60 270 0 196Z" fill="var(--orange-deep)"/>
    <path d="M0 196 Q60 270 170 292 Q300 312 450 252 V260 Q300 322 160 302 Q50 280 0 206Z" fill="var(--green)"/>
    <circle cx="91" cy="232" r="60" fill="var(--white)" stroke="var(--orange-deep)" stroke-width="5"/>
    <path d="M0 548 Q225 385 450 548 V600 H0Z" fill="#d8d8d8"/>
    <path d="M0 560 Q225 400 450 560 V1036 H0Z" fill="url(#fOrange)"/>
    <circle cx="225" cy="508" r="26" fill="none" stroke="var(--rust)" stroke-width="2"/>
    <g fill="none" stroke="var(--rust)" stroke-width="2.2" stroke-linejoin="round">
      <path d="M230 494 l8 8 l-12 12 l-8 -8Z"/>
      <path d="M218 506 l-7 7 q-2 4 2 6 l4 -1 l9 -4"/>
    </g>
    <path d="M108 716 L340 708 L356 720 L338 734 L360 740 L110 746 L96 734 L116 728 L94 722Z" fill="url(#fRust)"/>
    <path d="M0 996 Q225 868 450 996 V1036 H0Z" fill="var(--green)"/>
    <path d="M0 1016 Q225 864 450 1016 V1036 H0Z" fill="url(#fFoot)"/>
  </svg>

  <p class="abs brand-name">Brightwall Coaters</p>
  <p class="abs tagline">TAKE CONTROL OF HOW YOUR HOME LOOKS!</p>

  <h1 class="abs headline headline--lead">We make your home look</h1>
  <p class="abs headline headline--main">CLEAN, FRESH &amp; BEAUTIFUL</p>
  <p class="abs headline headline--again">Again!</p>

  <h2 class="abs problem">Problem</h2>
  <p class="abs problem-copy">Your exterior semi-transparent deck,fence<br>or siding is peeling, chipping or faded.</p>

  <p class="abs estimates">FREE ESTIMATES</p>
  <p class="abs phone">647-555-0148</p>

  <div class="abs links">
    <p class="links__row"><span class="links__dot"></span>www.brightwallcoaters.com</p>
    <p class="links__row"><span class="links__dot"></span>social.brightwallcoaters.com</p>
  </div>
</section>

<section class="card card--back" aria-label="Back of rack card">
  <svg class="card__art" viewBox="0 0 450 1036">
    <defs>
      <linearGradient id="bSky" x1="0" y1="0" x2="1" y2="0">
        <stop offset="0" stop-color="#d9d9d9"/><stop offset=".5" stop-color="#f7f7f7"/><stop offset="1" stop-color="#e6e6e6"/>
      </linearGradient>
      <linearGradient id="bNight" x1="0" y1="0" x2="1" y2="1">
        <stop offset="0" stop-color="#2c3446"/><stop offset="1" stop-color="#141a26"/>
      </linearGradient>
      <linearGradient id="bPhoto" x1="0" y1="0" x2="0" y2="1">
        <stop offset="0" stop-color="#c7b8aa"/><stop offset=".55" stop-color="#e8c94a"/><stop offset="1" stop-color="#d8b83a"/>
      </linearGradient>
      <radialGradient id="bOrange" cx=".5" cy=".3" r=".8">
        <stop offset="0" stop-color="#faa54b"/><stop offset=".6" stop-color="#f78f20"/><stop offset="1" stop-color="#e4601a"/>
      </radialGradient>
      <linearGradient id="bRust" x1="0" y1="0" x2="1" y2="0">
        <stop offset="0" stop-color="#8c3408"/><stop offset=".5" stop-color="#b24a12"/><stop offset="1" stop-color="#8c3408"/>
      </linearGradient>
      <linearGradient id="bFoot" x1="0" y1="0" x2="0" y2="1">
        <stop offset="0" stop-color="#3a3a3a"/><stop offset="1" stop-color="#161616"/>
      </linearGradient>
    </defs>
    <rect width="450" height="420" fill="url(#bSky)"/>
    <path d="M340 100 Q400 70 450 80 V380 H300 Q320 220 340 100Z" fill="url(#bNight)" role="img" aria-label="Dark paint roller texture"/>
    <path d="M0 80 H60 V330 H0Z" fill="#cfcfcf" role="img" aria-label="Aluminium step ladder"/>
    <path d="M70 120 Q180 80 300 150 L330 330 H70Z" fill="url(#bPhoto)" role="img" aria-label="Photo of a thoughtful painter in a yellow shirt holding a paint roller"/>
    <path d="M0 392 Q225 198 450 392 V440 H0Z" fill="#d8d8d8"/>
    <path d="M0 408 Q225 216 450 408 V1036 H0Z" fill="url(#bOrange)"/>
    <path d="M40 446 L410 440 L421 470 L412 520 L420 560 L408 608 L36 604 L29 570 L38 530 L30 480Z" fill="url(#bRust)"/>
    <rect x="73" y="456" width="308" height="140" fill="none" stroke="var(--white)" stroke-width="2" stroke-dasharray="2 4"/>
    <path d="M52 624 L406 618 L418 650 L410 700 L420 744 L404 786 L40 782 L30 750 L40 704 L32 660Z" fill="url(#bRust)"/>
    <rect x="73" y="640" width="308" height="136" fill="none" stroke="var(--white)" stroke-width="2" stroke-dasharray="2 4"/>
    <path d="M0 996 Q225 868 450 996 V1036 H0Z" fill="var(--green)"/>
    <path d="M0 1016 Q225 864 450 1016 V1036 H0Z" fill="url(#bFoot)"/>
  </svg>

  <div class="abs brand">
    <span class="brand__disc"></span>
    <p class="brand-name">Brightwall Coaters</p>
  </div>

  <h2 class="abs offer-title">SPECIAL OFFER!</h2>

  <p class="abs offer offer--windows">If you are one of the<strong>first 17 exterior projects</strong>that book with us, you will<br>receive a complimentary<br>window cleaning!</p>
  <p class="abs offer offer--design">If you are one of the<strong>first 13 exterior projects</strong>that book with us, you will receive<br>a complimentary<br>interior design consultation by a<br>professional interior designer!</p>

  <p class="abs estimates">FREE ESTIMATES</p>
  <p class="abs phone">647-555-0148</p>

  <div class="abs links">
    <p class="links__row"><span class="links__dot"></span>www.brightwallcoaters.com</p>
    <p class="links__row"><span class="links__dot"></span>social.brightwallcoaters.com</p>
  </div>
</section>

</body>
</html>
```